indépendant en tant que Massothérapeute et Préparateur Mental, j'ai besoin de ...

Massothérapeute et préparateur mental indépendant, je recherche une carte de visite sobre et dynamique, sans images liées au massage ou à la préparation mentale mais intégrant mon logo. Les couleurs que j'aime bien sont : Blanc, gris, anthracite, noir et jaune

carte de préférence Horizontale
neutre qui puisse toucher le deux domaines Massothérapie et préparation mentale

Requirements
Must have
• mon projet doit intégrer au recto:
LOGO
Loïc Bardemaz
078 315 26 48
info@loicbardemaz-exemple.ch
et éventuellement www.loicbardemaz-exemple.ch

et au verso les deux adresses:

Chemin des Grèvelins 7B
1465 Valmorel-le-Lac

Avenue des Mélèzes 9
1726 Montbrevin

Should not have
• mon projet ne doit pas contenir d'image en liens avec le massage ni la préparation mentale.

```html
<!DOCTYPE html>
<html lang="fr">
<head>
<meta charset="utf-8">
<title>Loïc Bardemaz – Cartes de visite</title>
<link href="https://fonts.googleapis.com/css2?family=Work+Sans:wght@400;500;600&display=swap" rel="stylesheet">
<style>
  :root {
    --backdrop: #2b2b2b;
    --card: #ffffff;
    --ink: #1f1f1f;
    --anthracite: #3a3a3a;
    --yellow: #f6b80f;
  }
  * { margin: 0; padding: 0; box-sizing: border-box; }
  html, body { width: 1200px; height: 930px; overflow: hidden; }
  body {
    background: var(--backdrop);
    font-family: "Work Sans", Arial, sans-serif;
    color: var(--ink);
    position: relative;
  }
  .card {
    position: absolute;
    width: 560px;
    height: 320px;
    border-radius: 22px;
    overflow: hidden;
    background: var(--card);
  }
  .card--front { left: 60px; top: 120px; }
  .card--back { left: 580px; top: 470px; }

  .front-visual {
    position: absolute; inset: 0;
    background: linear-gradient(135deg, #d9d6d5 0%, #bdb6b3 40%, #e9e8e8 75%, #f4f4f4 100%);
  }
  .front-brand {
    position: absolute; left: 150px; top: 128px;
    display: flex; align-items: center; gap: 12px;
  }
  .brand-mark { width: 14px; height: 14px; background: var(--anthracite); flex: none; }
  .brand-text { display: flex; flex-direction: column; }
  .brand-name { font-weight: 600; font-size: 26px; color: var(--anthracite); line-height: 1.1; }
  .brand-tagline { font-weight: 400; font-size: 10px; color: var(--anthracite); letter-spacing: 0.6px; text-transform: uppercase; margin-top: 3px; }

  .back-brand {
    position: absolute; right: 40px; top: 38px;
    display: flex; align-items: center; gap: 10px;
  }
  .back-brand .brand-name { font-size: 20px; }
  .back-brand .brand-tagline { font-size: 8px; }

  .accent-bar { position: absolute; left: 0; top: 132px; width: 7px; height: 44px; background: var(--yellow); }
  .holder { position: absolute; left: 40px; top: 128px; }
  .holder-name { font-size: 24px; font-weight: 500; color: var(--yellow); letter-spacing: 1px; text-transform: uppercase; line-height: 1.1; }
  .holder-role { font-size: 15px; color: var(--ink); margin-top: 2px; }
  .divider { position: absolute; left: 40px; right: 40px; top: 190px; height: 1.5px; background: var(--yellow); }

  .contacts { position: absolute; left: 40px; bottom: 28px; list-style: none; }
  .contacts li { display: flex; align-items: center; gap: 10px; font-size: 15px; line-height: 23px; }
  .contacts svg { width: 11px; height: 11px; flex: none; }

  .addresses { position: absolute; right: 40px; top: 206px; text-align: right; font-size: 14px; line-height: 18px; }
  .address-sep { width: 14px; height: 1.5px; background: var(--yellow); margin: 7px 0 7px auto; }
</style>
</head>
<body>
  <section class="card card--front">
    <div class="front-visual" role="img" aria-label="Fond photographique clair en tons gris et blancs"></div>
    <div class="front-brand">
      <span class="brand-mark"></span>
      <div class="brand-text">
        <span class="brand-name">Loïc Bardemaz</span>
        <span class="brand-tagline">Massothérapeute / Préparateur Mental</span>
      </div>
    </div>
  </section>

  <section class="card card--back">
    <div class="back-brand">
      <span class="brand-mark"></span>
      <div class="brand-text">
        <span class="brand-name">Loïc Bardemaz</span>
        <span class="brand-tagline">Massothérapeute / Préparateur Mental</span>
      </div>
    </div>

    <span class="accent-bar"></span>
    <div class="holder">
      <p class="holder-name">Loïc Bardemaz</p>
      <p class="holder-role">Director</p>
    </div>
    <span class="divider"></span>

    <ul class="contacts">
      <li>
        <svg viewBox="0 0 24 24" aria-hidden="true"><path fill="#f6b80f" d="M6.6 10.8a15 15 0 0 0 6.6 6.6l2.2-2.2c.3-.3.7-.4 1-.2 1.1.4 2.3.6 3.6.6.6 0 1 .4 1 1V20c0 .6-.4 1-1 1A17 17 0 0 1 3 4c0-.6.4-1 1-1h3.5c.6 0 1 .4 1 1 0 1.3.2 2.5.6 3.6.1.3 0 .7-.2 1z"/></svg>
        078 315 26 48
      </li>
      <li>
        <svg viewBox="0 0 24 24" aria-hidden="true"><rect x="2" y="5" width="20" height="14" rx="2" fill="none" stroke="#f6b80f" stroke-width="2.4"/><path d="M3 6l9 7 9-7" fill="none" stroke="#f6b80f" stroke-width="2.4"/></svg>
        info@loicbardemaz-exemple.ch
      </li>
      <li>
        <svg viewBox="0 0 24 24" aria-hidden="true"><circle cx="12" cy="12" r="10" fill="#f6b80f"/><path d="M2 12h20M12 2c3 3 3 17 0 20M12 2c-3 3-3 17 0 20" fill="none" stroke="#fff" stroke-width="1.4"/></svg>
        www.loicbardemaz-exemple.ch
      </li>
    </ul>

    <div class="addresses">
      <p>Chemin des Grèvelins 7B</p>
      <p>1465 Valmorel-le-Lac</p>
      <div class="address-sep"></div>
      <p>Avenue des Mélèzes 9</p>
      <p>1726 Montbrevin</p>
    </div>
  </section>
</body>
</html>
```